My colors are BLACK, WHITE AND RED. I want something super professional but feminine and a bit sassy. My original logo is gold and black, I would like to see the crown in red (still with gradient) . I have a suggested layout in the files but am totally open to fresh ideas. I'm torn about having a little crown on the front as well as large logo on the back.

Target Market(s)

People buying high end houses

Font styles to use
Serif
Sans Serif

Requirements
Must have
• all the verbiage and text needed is on the business card in the files.
Nice to have
• classy, pretty, elegant, business like
Should not have
• cheesy, guady, boring

```html
<!DOCTYPE html>
<html lang="en">
<head>
<meta charset="UTF-8">
<title>Vivian Ashcroft – Business Card</title>
<link rel="stylesheet" href="https://fonts.googleapis.com/css2?family=Cinzel:wght@500;600&family=Questrial&display=swap">
<style>
  :root {
    --stage: #1e1e1e;
    --card-black: #050505;
    --card-white: #ffffff;
    --ink: #111111;
    --red: #e31b23;
    --red-deep: #b8121a;
    --photo-warm: #c98a5a;
    --photo-dark: #2b2b2e;
  }
  * { box-sizing: border-box; margin: 0; padding: 0; }
  html, body {
    width: 1200px;
    height: 1200px;
    overflow: hidden;
    background: var(--stage);
  }
  .canvas {
    position: relative;
    width: 1200px;
    height: 1200px;
    display: flex;
    flex-direction: column;
    align-items: center;
    justify-content: center;
    gap: 36px;
  }
  .card {
    position: relative;
    width: 900px;
    height: 514px;
    overflow: hidden;
  }

  /* Back of card */
  .card--back {
    background: var(--card-black);
    display: flex;
    align-items: center;
    justify-content: center;
  }
  .brand-mark {
    display: flex;
    align-items: center;
    gap: 22px;
  }
  .brand-mark__dot {
    width: 22px;
    height: 22px;
    border-radius: 50%;
    background: linear-gradient(135deg, var(--red), var(--red-deep));
  }
  .brand-mark__name {
    font-family: "Cinzel", serif;
    font-weight: 500;
    font-size: 54px;
    letter-spacing: 0.18em;
    color: var(--card-white);
  }

  /* Front of card */
  .card--front {
    background: var(--card-white);
  }
  .front__band {
    position: absolute;
    left: 0;
    bottom: 0;
    width: 600px;
    height: 26px;
    background: var(--red);
  }
  .front__photo {
    position: absolute;
    right: 0;
    bottom: 0;
    width: 370px;
    height: 420px;
    background: radial-gradient(ellipse at 55% 25%, var(--photo-warm) 0%, #b97a4e 30%, var(--photo-dark) 62%, #3a3a3d 100%);
  }
  .front__info {
    position: absolute;
    left: 70px;
    top: 70px;
  }
  .agent-name {
    display: flex;
    align-items: center;
    gap: 16px;
  }
  .agent-name__text {
    font-family: "Cinzel", serif;
    font-weight: 600;
    font-size: 46px;
    letter-spacing: 0.02em;
    color: var(--ink);
    line-height: 1;
  }
  .agent-name__dot {
    width: 16px;
    height: 16px;
    border-radius: 50%;
    background: var(--red);
  }
  .agent-title {
    margin-top: 8px;
    font-family: "Questrial", sans-serif;
    font-size: 22px;
    letter-spacing: 0.3em;
    color: var(--ink);
  }
  .credentials {
    list-style: none;
    margin-top: 28px;
    font-family: "Questrial", sans-serif;
    font-size: 23px;
    line-height: 1.5;
    color: var(--ink);
  }
  .contact {
    list-style: none;
    margin-top: 26px;
    font-family: "Questrial", sans-serif;
    font-size: 25px;
    color: var(--ink);
  }
  .contact__item {
    display: flex;
    align-items: center;
    gap: 14px;
    margin-bottom: 8px;
  }
  .contact__icon {
    width: 28px;
    height: 28px;
    flex: none;
  }
</style>
</head>
<body>
<main class="canvas">

  <section class="card card--back" aria-label="Card back">
    <div class="brand-mark">
      <span class="brand-mark__dot"></span>
      <span class="brand-mark__name">VIVIAN ASHCROFT</span>
    </div>
  </section>

  <section class="card card--front" aria-label="Card front">
    <div class="front__info">
      <div class="agent-name">
        <h1 class="agent-name__text">VIVIAN ASHCROFT</h1>
        <span class="agent-name__dot"></span>
      </div>
      <p class="agent-title">REAL ESTATE AGENT</p>
      <ul class="credentials">
        <li>Certified Mountain Area Specialist</li>
        <li>Certified Luxury Home Marketing Specialist</li>
        <li>Certified Negotiation Expert</li>
      </ul>
      <ul class="contact">
        <li class="contact__item">
          <svg class="contact__icon" viewBox="0 0 28 28" aria-hidden="true">
            <circle cx="14" cy="14" r="13" fill="var(--red)"/>
            <circle cx="14" cy="14" r="10" fill="none" stroke="#fff" stroke-width="1.2"/>
            <path d="M10.5 8.5c.6-.4 1.3-.3 1.7.3l1 1.6c.3.5.2 1.1-.2 1.5l-.7.6c.6 1.3 1.6 2.4 2.9 3l.6-.7c.4-.4 1-.5 1.5-.2l1.6 1c.6.4.7 1.1.3 1.7l-.6.8c-.6.7-1.6.9-2.5.5-2.8-1.2-5-3.4-6.2-6.2-.4-.9-.2-1.9.5-2.5z" fill="#fff"/>
          </svg>
          <span>720-555-0184</span>
        </li>
        <li class="contact__item">
          <svg class="contact__icon" viewBox="0 0 28 28" aria-hidden="true">
            <circle cx="14" cy="14" r="13" fill="var(--red)"/>
            <circle cx="14" cy="14" r="10" fill="none" stroke="#fff" stroke-width="1.2"/>
            <rect x="8.5" y="10" width="11" height="8" rx="1" fill="#fff"/>
            <path d="M8.8 10.4 14 14.6l5.2-4.2" fill="none" stroke="var(--red)" stroke-width="1.1"/>
          </svg>
          <span>vashcroft@homesmail.net</span>
        </li>
      </ul>
    </div>
    <div class="front__band"></div>
    <div class="front__photo" role="img" aria-label="Portrait photo of the agent in a dark blazer, hands on hips"></div>
  </section>

</main>
</body>
</html>
```